Holiday Rental Company Flyer Design (DL not A5)

Note from PixelFolk Administration: The category sizing selected is A5, however the project requires DL sized artwork. Please refer to the DL template link below while the 'Special Requirements' are updated accordingly.

Project Brief:
We need a double sided DL flyer designed for an up market Holiday Rental Company that portrays a personalised approach to property management. These are to be used for letter box drops to homes we're specifically targeting so the design should be modern, complimentary colour palette, uncluttered & visually appealing.

Please Download the DL Template from Quillmark here: http://www.quillmark.com.au/qm/ns/propath/UploadResources.aspx?selectedTab=0?pfid=BFB&pf_id=BFB&xnav=easypath-upload-image#Templates

Target Market(s)

Wealthy Home Owners

Industry/Entity Type

It Company

Font styles to use
Other font styles liked:
• Avant Garde Extra Light & Demi

Colors
33b8a4

Requirements
Must have
• DL Flyer sizes (210mm width x 99mm width, plus 3mm bleed)
• Front: Logo, Main Image & Grab
• Back: Contact Details & Brief Description of our business
• Images: Ideally the main image should be the house with the pool but alternatively a lifestyle images could also be used.
Nice to have
• A creative designer!
Should not have
• Clutter & busy designs

```html
<!DOCTYPE html>
<html lang="en">
<head>
<meta charset="utf-8">
<title>Harbourline Stays – DL Flyer</title>
<link href="https://fonts.googleapis.com/css2?family=Questrial&family=Poppins:wght@300;600&display=swap" rel="stylesheet">
<style>
  :root {
    --page: #ffffff;
    --card: #ffffff;
    --grey-band: #cfd0d1;
    --logo-grey: #7d7e80;
    --text-dark: #4a4a4c;
    --teal: #33b8a4;
    --orange: #c95f1e;
    --lilac: rgba(150, 138, 190, 0.85);
    --veil: rgba(120, 110, 170, 0.35);
    --shadow: 0 2px 6px rgba(0, 0, 0, 0.35);
  }
  * { box-sizing: border-box; margin: 0; padding: 0; }
  html, body { width: 1200px; height: 1200px; overflow: hidden; background: var(--page); }
  body { position: relative; font-family: "Questrial", "Poppins", sans-serif; color: var(--text-dark); }

  .flyer { position: absolute; background: var(--card); box-shadow: var(--shadow); overflow: hidden; }
  .flyer--front { left: 104px; top: 100px; width: 667px; height: 476px; }
  .flyer--back  { left: 444px; top: 620px; width: 667px; height: 473px; }

  .wordmark {
    position: absolute; color: var(--logo-grey); font-family: "Questrial", sans-serif;
    font-weight: 400; letter-spacing: 2px; line-height: 1.05; text-transform: uppercase;
  }
  .flyer--front .wordmark { left: 428px; top: 52px; font-size: 27px; }
  .flyer--back .wordmark  { left: 54px; top: 44px; font-size: 25px; text-align: center; }
  .wordmark-dot {
    position: absolute; left: -34px; top: 14px; width: 26px; height: 26px;
    border: 1.5px solid var(--logo-grey); border-radius: 50%;
  }

  .hero-photo {
    position: absolute; left: 0; top: 127px; width: 583px; height: 349px;
    background: linear-gradient(160deg, #1b1a4a 0%, #3a2f6b 35%, #6b5a3a 55%, #1d5fb8 80%, #4fb6ef 100%);
  }
  .tagline {
    position: absolute; left: 284px; top: 155px; width: 299px; height: 37px;
    background: var(--veil); color: var(--teal); font-family: "Poppins", sans-serif;
    font-weight: 300; font-size: 14.5px; line-height: 37px; padding-left: 26px;
  }
  .tagline-accent {
    position: absolute; left: 473px; top: 189px; width: 194px; height: 37px;
    background: var(--lilac); color: var(--orange); font-family: "Poppins", sans-serif;
    font-weight: 600; font-size: 18px; line-height: 38px; padding-left: 36px; letter-spacing: 0.5px;
  }

  .grey-band { position: absolute; left: 0; top: 167px; width: 100%; height: 306px; background: var(--grey-band); }
  .subhead {
    position: absolute; left: 52px; top: 116px; color: var(--orange);
    font-size: 13px; letter-spacing: 0.5px; text-transform: uppercase;
  }
  .lifestyle-photo {
    position: absolute; top: 83px; width: 112px; height: 112px; border-radius: 50%;
    border: 3px solid #fff; box-shadow: 0 0 3px rgba(0,0,0,0.2);
  }
  .lifestyle-photo--living { left: 275px; background: radial-gradient(circle at 40% 60%, #e2c23a, #b89a5a 60%, #d8cfc2); }
  .lifestyle-photo--flowers { left: 403px; background: radial-gradient(circle at 50% 40%, #d9772c, #7d6a58 55%, #5a6d7d); }
  .lifestyle-photo--bath { left: 533px; background: radial-gradient(circle at 45% 50%, #f1f1ef, #bfc0c0 65%, #9a9b9c); }

  .about { position: absolute; left: 47px; top: 192px; width: 248px; font-size: 11px; line-height: 1.3; }
  .about p { margin-bottom: 13px; }
  .about em { font-style: italic; font-weight: 600; font-family: "Poppins", sans-serif; font-size: 10.5px; }
  .benefits { list-style: none; margin-top: 4px; }
  .benefits li { position: relative; padding-left: 36px; margin-bottom: 12px; min-height: 24px; }
  .benefits li::before {
    content: ""; position: absolute; left: 0; top: 1px; width: 23px; height: 23px;
    border-radius: 50%; background: var(--orange);
  }

  .divider {
    position: absolute; left: 332px; top: 220px; width: 0; height: 222px;
    border-left: 3px dotted #fff;
  }
  .contact { position: absolute; left: 376px; top: 244px; width: 250px; font-size: 11px; line-height: 1.3; }
  .contact-details { margin-top: 24px; color: var(--teal); }
  .contact-address { margin-top: 16px; color: var(--teal); }
  .web-bar {
    position: absolute; left: 440px; top: 404px; width: 227px; height: 24px;
    background: var(--orange); color: #fff; font-size: 12px; line-height: 24px; padding-left: 32px;
  }
</style>
</head>
<body>

  <section class="flyer flyer--front">
    <div class="wordmark"><span class="wordmark-dot"></span>Harbourline<br>Stays</div>
    <div class="hero-photo" role="img" aria-label="Modern luxury home at dusk with lit interior and illuminated blue pool with water feature"></div>
    <div class="tagline">Holiday Rental Management with a</div>
    <div class="tagline-accent">DIFFERENCE</div>
  </section>

  <section class="flyer flyer--back">
    <div class="grey-band"></div>
    <div class="wordmark">Harbourline<br>Stays</div>
    <div class="subhead">What we do differently!</div>

    <div class="lifestyle-photo lifestyle-photo--living" role="img" aria-label="Yellow cushions on a styled lounge"></div>
    <div class="lifestyle-photo lifestyle-photo--flowers" role="img" aria-label="Orange flowers in a glass vase on a table"></div>
    <div class="lifestyle-photo lifestyle-photo--bath" role="img" aria-label="White bathroom basin with chrome tap"></div>

    <div class="about">
      <p>Rather than relying upon a key safe or a central pick-up destination, a <em>Harbourline Stays</em> staff member will greet guests upon arrival.</p>
      <p>Our 'Meet &amp; Greet' service provides home owners with an increased level of Security and also allows us to:</p>
      <ul class="benefits">
        <li>Prepare the home for their arrival (lights, heaters, music etc.)</li>
        <li>Establish a rapport &amp; help facilitate future bookings</li>
        <li>Reiterate their responsibilities to ensure the return of their bond</li>
      </ul>
    </div>

    <div class="divider"></div>

    <div class="contact">
      <p>If you'd like to know what your property could achieve or require additional information, please contact us:</p>
      <p class="contact-details">t: (03)5550 0142<br>e: stay@harbourlinestays.com.au</p>
      <p class="contact-address">PO Box 48, Tidewater Victoria 3999</p>
    </div>

    <div class="web-bar">harbourlinestays.com.au</div>
  </section>

</body>
</html>
```